Podcast cover art (not a logo)

I’m launching an audio-only podcast for parents of neurodivergent children. The podcast is meant to feel like a calm, trusted professional voice — not a brand or a performance.

Style direction:
--Clean and minimal
--Calm and grounded
--Professional, not playful
--Nothing flashy, loud, or busy
--No cartoon imagery

Content on the cover:
--Podcast title: Under the Quiet Surface
--Subtitle or tagline: Guiding Neurodivergent Children with Evidence, Not Blame (or Making Sense of Neurodivergent Minds)
--No episode numbers, no dates

Design preferences:
--Text-forward design
--Neutral or soft colors (muted blues, grays, off-whites)
--High contrast for readability at small sizes
--Simple, timeless font

What I do NOT want:
--A logo or branding system
--Illustrations of children or families
--Bright colors or playful graphics
--Trendy fonts or visual effects

Technical requirements:
--Square image
--3000 × 3000 pixels
--RGB color mode
--JPEG or PNG
--File size under 500 KB

Deliverables:
--Final cover art file
--Optional: one or two alternate background color versions

```html
<!DOCTYPE html>
<html lang="en">
<head>
<meta charset="utf-8">
<title>Under the Quiet Surface — Podcast Cover</title>
<link rel="stylesheet" href="https://fonts.googleapis.com/css2?family=Anton&family=Oswald:wght@300;700&display=swap">
<style>
  :root {
    --cover-blue: #8aaec4;
    --accent-brown: #7f5949;
    --text-white: #ffffff;
    --decor-blue: #a3bfd2;
  }
  html, body {
    margin: 0;
    padding: 0;
    width: 1200px;
    height: 1200px;
    overflow: hidden;
    background: var(--cover-blue);
  }
  .cover {
    position: relative;
    width: 1200px;
    height: 1200px;
    background: var(--cover-blue);
    overflow: hidden;
  }
  .cover-decoration {
    position: absolute;
    left: 662px;
    top: 175px;
    width: 538px;
    height: 868px;
    background: radial-gradient(ellipse at 75% 45%, rgba(163,191,210,0.7) 0%, rgba(163,191,210,0.3) 50%, rgba(163,191,210,0) 75%);
  }
  h1 { margin: 0; }
  .title-light,
  .title-bold,
  .tagline,
  .tagline-alt {
    position: absolute;
    left: 96px;
    margin: 0;
    line-height: 1;
    white-space: nowrap;
  }
  .title-light {
    top: 145px;
    font-family: "Oswald", sans-serif;
    font-weight: 300;
    font-size: 140px;
    color: var(--text-white);
  }
  .title-bold {
    top: 273px;
    font-family: "Anton", sans-serif;
    font-weight: 400;
    font-size: 250px;
    color: var(--accent-brown);
  }
  .title-rule {
    position: absolute;
    left: 96px;
    top: 593px;
    width: 179px;
    height: 22px;
    background: var(--accent-brown);
  }
  .tagline {
    font-family: "Oswald", sans-serif;
    font-weight: 700;
    font-size: 78px;
    letter-spacing: -2px;
    color: var(--text-white);
  }
  .tagline-alt {
    font-family: "Oswald", sans-serif;
    font-weight: 300;
    font-size: 78px;
    letter-spacing: -2px;
    color: var(--text-white);
  }
  .line-1 { top: 673px; }
  .line-2 { top: 771px; }
  .line-3 { top: 865px; }
  .line-4 { top: 963px; }
</style>
</head>
<body>
  <main class="cover">
    <div class="cover-decoration" role="img" aria-label="Faint microphone and sound-level bars decoration"></div>

    <h1>
      <span class="title-light">Under the Quiet</span>
      <span class="title-bold">Surface</span>
    </h1>

    <div class="title-rule"></div>

    <p class="tagline line-1">Guiding Neurodivergent Children</p>
    <p class="tagline line-2">with Evidence, Not Blame</p>
    <p class="tagline-alt line-3">(or Making Sense of</p>
    <p class="tagline-alt line-4">Neurodivergent Minds)</p>
  </main>
</body>
</html>
```